Website redesign

PLOBrisk.com is a website that allows real estate investors to search for and find investment grade residential real estate property. The website is up and running, but is in desperate need of a facelift. You can see the existing website at http://www.plobrisk.example. PLO stands for "Real Estate Investor" by the way.
We just finished our design competition for our logo and are now ready to move on to the website design itself!
The industry is real estate, but it is really just focused on the investor market, so we do not cater to the married couple looking to buy their next house. Our clients are business people searching for properties to buy so they can either resell them at a profit or hold them and rent them out.
On the PLOBrisk website, the real estate investor can search for properties using a unique search engine that focuses on the financial aspects of property. Once they find a property, the website allows them to quickly and easily make offers on those properties (investment real estate is sometimes a volume game - you might make offers on 20 houses to secure 1 house).
This website is not about "get rich quick" kind of stuff, so designs with a bunch of dollar signs, or things like that is not what I am looking for.
The design should be tailored to the business person (the real estate investor). Thus, it should be serious, but at the same time have a little edge to it.
We are looking to use modern design elements including:
- A Flat Design - no 3D please
- Large Hero Area – with eye catching imagery and verbiage
- Long scrolling page, but sparse content
- Simple color scheme – bold colors ok, but don’t need all the colors of the rainbow represented
- Larger fonts but with less content. More calls to action
- I would really like to investigate the use of cards for our search results. I’m not convinced this will work, but if we can make it work I think it would be impressive.
IMPORTANT: Out site is a gridkit website, so please ensure that the designs you come up with are capable of being implemented in Quillon GridKit.
If you are a killer designer, there will be more work to come for you as we have a long list of enhancements that will require ongoing UI work.
I will participate heavily in this project, so ask me your questions and I will get back to you very quickly.
Examples of designs that I like:
http://www.vendrapo.example/
http://www.lumestrandstudio.example/
http://www.hobrenta.example
http://www.casqino.example
http://www.pexmoraweb.example/
Your Deliverables:
- 2 Page Concepts:
o Home Page: http://www.plobrisk.example
o Search Page: http://www.plobrisk.example/s/Dallas/flip-houses

```html
<!DOCTYPE html>
<html lang="en">
<head>
<meta charset="utf-8">
<title>PLOBrisk.com – Home</title>
<link href="https://fonts.googleapis.com/css2?family=Oswald:wght@400;500&family=Open+Sans:wght@400;600;700&display=swap" rel="stylesheet">
<style>
:root{
  --blue:#2b8fd8;
  --blue-light:#5aaee6;
  --blue-deep:#2271b3;
  --footer-bar:#1b5a91;
  --orange:#f6a31b;
  --ink:#2d2d2d;
  --muted:#777;
  --line:#dcdcdc;
  --paper:#ffffff;
  --grey-band:#ededed;
}
*{margin:0;padding:0;box-sizing:border-box}
html,body{width:1200px;height:2320px;overflow:hidden;background:var(--paper)}
body{font-family:"Open Sans",Arial,sans-serif;color:var(--ink)}
.page{position:relative;width:1200px;height:2320px;overflow:hidden}
.abs{position:absolute}
h1,h2,h3,.oswald{font-family:"Oswald","Arial Narrow",sans-serif;font-weight:500}

/* header */
.site-header{left:0;top:0;width:1200px;height:100px;background:var(--paper);border-bottom:1px solid var(--line)}
.brand{left:40px;top:30px;display:flex;align-items:center;gap:12px}
.brand-mark{width:36px;height:36px;background:var(--blue);border-radius:50%}
.brand-name{font-size:30px;font-weight:700;color:var(--blue)}
.account{right:40px;top:12px;font-size:12px;color:var(--muted)}
.account b{color:var(--blue);font-weight:600}
.main-nav{right:40px;top:52px;display:flex;gap:0}
.main-nav a{font-size:13px;font-weight:600;color:var(--ink);text-decoration:none;padding:6px 14px;border-left:1px solid var(--line);text-transform:uppercase}
.main-nav a:first-child{border-left:0;color:var(--blue)}

/* hero */
.hero{left:0;top:100px;width:1200px;height:500px;background:radial-gradient(ellipse at 55% 45%,#c08a4c 0%,#5b4a3c 22%,#2d3440 50%,#1c2230 100%)}
.hero-title{left:0;top:226px;width:1200px;text-align:center;color:#fff}
.hero-title h1{font-size:50px;font-weight:500;letter-spacing:.5px}
.hero-title p{font-size:22px;margin-top:-2px}
.search-tabs{left:300px;top:430px;display:flex}
.search-tabs span{font-size:13px;font-weight:600;color:#fff;padding:10px 16px}
.tab-flip{background:var(--blue)}
.tab-rent{background:var(--blue-light)}
.tab-adv{background:var(--orange)}
.search-panel{left:300px;top:468px;width:600px;height:92px;background:var(--paper);padding:12px 16px}
.search-panel .hint{font-size:12px;color:var(--muted)}
.search-fields{display:flex;gap:12px;margin-top:8px;align-items:flex-end}
.field label{display:block;font-size:11px;color:var(--muted);margin-bottom:2px}
.field .box{border:1px solid #c8c8c8;height:30px;font-size:13px;padding:5px 8px;display:flex;justify-content:space-between;align-items:center}
.btn-search{background:var(--orange);color:#fff;font-weight:700;font-size:14px;height:30px;padding:5px 22px;display:flex;align-items:center;gap:8px}

/* intro */
.intro{left:0;top:618px;width:1200px;text-align:center}
.intro h2{font-size:46px;color:var(--ink)}
.intro p{font-size:15px;color:var(--muted);margin-top:2px}

/* feature bands */
.band{top:750px;width:600px;height:110px;display:flex;align-items:center;gap:22px;color:#fff}
.band-find{left:0;background:var(--blue);padding-left:150px}
.band-buy{left:600px;background:var(--orange);padding-left:110px}
.band-icon{width:66px;height:66px;border-radius:50%;background:rgba(255,255,255,.22);display:flex;align-items:center;justify-content:center;flex:none}
.band h3{font-size:30px;font-weight:400;line-height:1.1}
.band p{font-size:12px;width:300px;line-height:1.4}
.band-pointer{left:190px;top:858px}

/* cards */
.card{top:900px;width:280px;height:470px;background:var(--paper);border:1px solid var(--line)}
.card h3{font-family:"Open Sans",Arial,sans-serif;font-weight:600;font-size:17px;text-align:center;padding:16px 0 12px}
.card-shot{margin:0 20px;height:200px;border:1px solid var(--line)}
.shot-site{background:linear-gradient(180deg,#dfe9f3 0 18%,#f6f6f6 18% 100%)}
.shot-filters{background:linear-gradient(180deg,#f5f5f5,#e9eef3)}
.shot-street{background:linear-gradient(160deg,#9fb8c9,#6d7f5d 60%,#4c5a48)}
.card-body{padding:16px 22px;font-size:13px;line-height:1.7;color:#555}
.card-body strong{color:var(--ink);font-weight:600;display:block;margin-bottom:2px}
.card-body ul{list-style:none}
.card-body li::before{content:"• ";color:var(--blue)}

/* demo */
.demo{left:0;top:1400px;width:1200px;height:680px;background:var(--grey-band)}
.demo h2{position:absolute;left:0;top:42px;width:1200px;text-align:center;font-size:46px}
.video{left:160px;top:130px;width:760px;height:480px;background:#111}
.video-bar{height:36px;background:#1e1e1e;color:#eee;font-size:14px;padding:9px 14px}
.video-stage{height:444px;background:linear-gradient(180deg,#e9edf1,#cfd6dd);position:relative}
.play{position:absolute;left:340px;top:182px}
.demo-side{left:940px;top:130px;width:130px}
.demo-item{margin-bottom:26px}
.demo-thumb{height:86px;background:linear-gradient(160deg,#b8c7d4,#7f8f6e);border:1px solid #cfcfcf}
.demo-item p{font-size:12px;line-height:1.45;color:#444;margin-top:8px}

/* footer */
.site-footer{left:0;top:2080px;width:1200px;height:200px;background:var(--blue-deep);color:#dce9f5}
.f-col{top:30px;width:220px;font-size:11.5px;line-height:1.6}
.f-col h4{font-size:15px;font-weight:600;color:#fff;margin-bottom:10px}
.f-col .post{margin-bottom:6px}
.f-col .post small{display:block;color:#9fc2e2;font-size:10px}
.f-input{display:flex;margin-top:10px}
.f-input span{flex:1;background:#fff;color:#999;font-size:11px;padding:6px 8px}
.f-input b{background:var(--orange);width:30px}
.contact-row{display:flex;gap:8px;align-items:flex-start;margin-bottom:5px}
.legal{left:0;top:2280px;width:1200px;height:40px;background:var(--footer-bar);color:#bcd3e8;font-size:11px;padding:12px 160px}
</style>
</head>
<body>
<div class="page">

  <header class="site-header abs">
    <div class="brand abs"><span class="brand-mark"></span><span class="brand-name">PLOBrisk.com</span></div>
    <div class="account abs"><b>SIGN IN</b> &nbsp;|&nbsp; <b>SIGN UP</b></div>
    <nav class="main-nav abs">
      <a href="#">Home</a><a href="#">Properties</a><a href="#">About Us</a><a href="#">Speed Offer</a><a href="#">Agents</a>
    </nav>
  </header>

  <section class="hero abs" role="img" aria-label="Photograph of a modern lit house at dusk"></section>
  <div class="hero-title abs">
    <h1>Start Your Search</h1>
    <p>What kind of investor are you?</p>
  </div>
  <div class="search-tabs abs">
    <span class="tab-flip">I am flipping properties</span>
    <span class="tab-rent">I am buying &amp; renting properties</span>
    <span class="tab-adv">I am an advanced user</span>
  </div>
  <form class="search-panel abs">
    <div class="hint">Show me properties with the MOST potential equity.</div>
    <div class="search-fields">
      <div class="field" style="width:190px"><label>City</label><div class="box">Dallas <span>▾</span></div></div>
      <div class="field" style="width:220px"><label>Distance from city center</label><div class="box">Miles</div></div>
      <div class="btn-search">
        <svg width="14" height="14" viewBox="0 0 14 14"><circle cx="6" cy="6" r="4.5" fill="none" stroke="#fff" stroke-width="2"/><line x1="9.5" y1="9.5" x2="13" y2="13" stroke="#fff" stroke-width="2"/></svg>Search
      </div>
    </div>
  </form>

  <section class="intro abs">
    <h2>What is PLOBrisk?</h2>
    <p>PLOBrisk was designed by Real Estate Investors for Real Estate Investors</p>
  </section>

  <div class="band band-find abs">
    <div class="band-icon"><svg width="34" height="34" viewBox="0 0 34 34"><circle cx="14" cy="14" r="10" fill="none" stroke="#fff" stroke-width="3"/><line x1="21" y1="21" x2="31" y2="31" stroke="#fff" stroke-width="4"/></svg></div>
    <div><h3>Find Properties</h3><p>Search for properties using criteria that matter to investors</p></div>
  </div>
  <svg class="band-pointer abs" width="40" height="20" viewBox="0 0 40 20"><polygon points="0,0 40,0 20,20" fill="#2b8fd8"/></svg>
  <div class="band band-buy abs">
    <div class="band-icon"><svg width="36" height="34" viewBox="0 0 36 34"><polygon points="18,3 33,16 29,16 29,31 7,31 7,16 3,16" fill="none" stroke="#fff" stroke-width="3" stroke-linejoin="round"/></svg></div>
    <div><h3>Buy Properties</h3><p>Make offers on properties with one click using the PLOBrisk Speed Offer Machine</p></div>
  </div>

  <article class="card abs" style="left:160px">
    <h3>Find a property</h3>
    <div class="card-shot shot-site" role="img" aria-label="Screenshot of the property search results page"></div>
    <div class="card-body"><strong>Search by:</strong>
      <ul><li>Estimated Equity</li><li>Price per Square Ft</li><li>GRM - Gross Rent Multiplier</li><li>GIM - Gross Income Multiplier</li><li>Capitalization Rate</li><li>Foreclosures</li></ul>
    </div>
  </article>
  <article class="card abs" style="left:460px">
    <h3>Personalize your search</h3>
    <div class="card-shot shot-filters" role="img" aria-label="Screenshot of the search filter buttons"></div>
    <div class="card-body"><strong>Filters designed just for investors</strong>
      <ul><li>Distressed Investment Properties</li><li>Fixed Rate Rentals</li><li>Off-Search Criteria</li><li>Search by Distance from City</li></ul>
    </div>
  </article>
  <article class="card abs" style="left:760px">
    <h3>Integration with top sites</h3>
    <div class="card-shot shot-street" role="img" aria-label="Street view photograph of a house"></div>
    <div class="card-body"><strong>All the data at your fingertips</strong>
      <ul><li>Hobrenta integration</li><li>Mapvale Maps</li><li>Mapvale Street View</li></ul>
    </div>
  </article>

  <section class="demo abs">
    <h2>See the Demo</h2>
    <div class="video abs">
      <div class="video-bar">PLOBrisk - Property Search Demo</div>
      <div class="video-stage" role="img" aria-label="Video preview showing the property search screen">
        <svg class="play" width="80" height="80" viewBox="0 0 80 80"><circle cx="40" cy="40" r="38" fill="#333" fill-opacity=".85"/><polygon points="32,24 58,40 32,56" fill="#fff"/></svg>
      </div>
    </div>
    <div class="demo-side abs">
      <div class="demo-item"><div class="demo-thumb" role="img" aria-label="Video thumbnail of a property search"></div><p>How to search the properties using PLOBrisk</p></div>
      <div class="demo-item"><div class="demo-thumb" role="img" aria-label="Video thumbnail of the offer screen"></div><p>How to make offers for properties using the PLOBrisk Speed Offer Machine</p></div>
    </div>
  </section>

  <footer class="site-footer abs">
    <div class="f-col abs" style="left:160px">
      <h4>About PLOBrisk</h4>
      <p>PLOBrisk is a search engine built for real estate investors to help them search, find and make offers on investment grade residential property.</p>
    </div>
    <div class="f-col abs" style="left:400px">
      <h4>Latest Posts</h4>
      <div class="post">How to value a rental property<small>12 Jan 2015 · 3 Comments</small></div>
      <div class="post">Five tips for your first flip<small>05 Jan 2015 · 2 Comments</small></div>
      <div class="post">Reading cap rate the right way<small>28 Dec 2014 · 4 Comments</small></div>
    </div>
    <div class="f-col abs" style="left:640px">
      <h4>Get in touch</h4>
      <div class="contact-row"><svg width="12" height="14" viewBox="0 0 12 14"><path d="M6 1a4.5 4.5 0 0 0-4.5 4.5C1.5 9 6 13 6 13s4.5-4 4.5-7.5A4.5 4.5 0 0 0 6 1z" fill="#fff"/></svg><span>214 Harlow Street, Suite 9, Dallas TX 75201</span></div>
      <div class="contact-row"><svg width="12" height="12" viewBox="0 0 12 12"><path d="M2 1h3l1 3-2 1a7 7 0 0 0 3 3l1-2 3 1v3c-6 0-9-3-9-9z" fill="#fff"/></svg><span>(555) 014-2290</span></div>
      <div class="contact-row"><svg width="12" height="10" viewBox="0 0 12 10"><rect x=".5" y=".5" width="11" height="9" fill="none" stroke="#fff"/><polyline points=".5,.5 6,5 11.5,.5" fill="none" stroke="#fff"/></svg><span>info@plobrisk.example</span></div>
    </div>
    <div class="f-col abs" style="left:880px">
      <h4>Subscribe</h4>
      <p>Subscribe for updates on new features and the latest PLOBrisk articles.</p>
      <div class="f-input"><span>Enter your e-mail</span><b></b></div>
    </div>
  </footer>
  <div class="legal abs">© 2015 PLOBrisk.com &nbsp;|&nbsp; Privacy Policy &nbsp;|&nbsp; Site Map</div>

</div>
</body>
</html>
```